Flyer-Design für Immobilienunternehmen
Zielgruppe
Verkauf von Immobilien und Grundstücken, Immobilienbewertung, Netzwerken in der Immobilienbranche
Private und gewerbliche Immobilien- und Grundstücksbesitzer, Erbengemeinschaften
Aufgabenstellung
Immobilienfachwirtin, Unternehmerin, Erfahrung,
Ich nehme mir Zeit für den Kunden

```html
<!DOCTYPE html>
<html lang="de">
<head>
<meta charset="utf-8">
<title>Brenner Immobilien – Flyer</title>
<link href="https://fonts.googleapis.com/css2?family=Questrial&family=Montserrat:wght@500;600&display=swap" rel="stylesheet">
<style>
:root{
  --bg:#e6e6e6;
  --paper:#ffffff;
  --green-dark:#5a8a3c;
  --green-mid:#7fae45;
  --green-light:#a9cf4c;
  --ink:#333333;
  --ink-soft:#666666;
  --photo-a:#c9c4bf;
  --photo-b:#e9e4de;
  --grad:linear-gradient(90deg,var(--green-dark),var(--green-light));
}
*{box-sizing:border-box;margin:0;padding:0}
html,body{width:750px;height:1200px;overflow:hidden;background:var(--bg)}
body{position:relative;font-family:"Questrial",sans-serif;color:var(--ink)}
.abs{position:absolute}
.sheet{position:absolute;left:98px;width:540px;background:var(--paper);overflow:hidden}
.sheet--outer{top:63px;height:505px}
.sheet--inner{top:634px;height:505px}
.photo{position:absolute;background:linear-gradient(135deg,var(--photo-a),var(--photo-b))}
.green-panel{position:absolute;background:linear-gradient(135deg,var(--green-dark) 20%,var(--green-light))}
.band{position:absolute;background:var(--grad);color:#fff;text-align:center;font-size:5.6px;line-height:6.6px;display:flex;align-items:center;justify-content:center}
.heading{position:absolute;display:flex;align-items:center;gap:6px;font-family:"Questrial",sans-serif;color:var(--ink);text-transform:uppercase}
.heading::before,.heading::after{content:"";flex:1;height:.6px;background:var(--green-mid)}
.heading--green{color:var(--green-dark)}
.body-text{position:absolute;font-size:5.2px;line-height:7.1px;color:var(--ink-soft)}
.body-text p{margin-bottom:6px}
.rule{width:20px;height:.6px;background:var(--green-mid);margin:0 0 8px}
.subhead{font-family:"Montserrat",sans-serif;font-weight:600;font-size:5.4px;line-height:7px;color:var(--ink);margin-bottom:7px;text-transform:uppercase}
.brand{position:absolute;display:flex;align-items:center;justify-content:center;gap:5px;font-family:"Questrial",sans-serif;color:var(--green-dark);letter-spacing:.5px}
.brand .dot{width:9px;height:9px;border-radius:50%;background:var(--green-mid)}
.slogan{position:absolute;color:#fff;text-align:center;font-family:"Questrial",sans-serif;text-transform:uppercase}
.contact-box{position:absolute;border:.8px solid #fff;color:#fff}
.contact-list{position:absolute;top:36px;left:0;right:0}
.contact-row{display:flex;align-items:center;gap:7px;font-size:6.6px;white-space:nowrap;margin:0 9px;height:21px;border-top:.6px solid rgba(255,255,255,.7)}
.contact-row svg{width:10px;height:10px;flex:none}
.url{position:absolute;font-family:"Montserrat",sans-serif;font-weight:500;font-size:8px;letter-spacing:.3px;text-align:center}
.icon{position:absolute;width:16px;height:16px}
.step-list{list-style:none}
.step-list li{display:flex;align-items:center;gap:6px;font-family:"Montserrat",sans-serif;font-weight:600;font-size:5.4px;color:#fff;height:17px}
.step-list span{width:10px;font-size:6px}
.mid-text{position:absolute;color:#fff;font-family:"Montserrat",sans-serif;font-weight:500;font-size:5.2px;line-height:7px}
</style>
</head>
<body>

<!-- ===== Outer side ===== -->
<section class="sheet sheet--outer">
  <!-- left panel -->
  <div class="photo" style="left:0;top:0;width:177px;height:136px" role="img" aria-label="Foto: Maklerin am Schreibtisch im Büro"></div>
  <div class="heading" style="left:0;top:158px;width:177px;font-size:10.5px">Immobilienverkauf</div>
  <div class="body-text" style="left:11px;top:188px;width:158px">
    <p>Eine Immobilie zu verkaufen, ob die eigene oder eine geerbte, geht nicht von heute auf morgen. Dessen ist man sich als Immobilienbesitzer bewusst. Ich verstehe mich als Partnerin an Ihrer Seite, die sich als lösungsorientierte Zuhörerin und Vermittlerin im Prozess Ihres Immobilienverkaufs sieht.</p>
    <div class="rule"></div>
    <p>Der Verkauf Ihrer Immobilie ist für mich nicht nur die Bewertung, das Erstellen eines Exposés und die Vertragsverhandlungen nach der Besichtigung. Mein Ziel ist es, gemeinsam mit Ihnen alle Aspekte des Verkaufs zu beleuchten, dazu braucht es Zeit und aktuelles Fachwissen. Beides können Sie von mir erwarten.</p>
    <div class="rule"></div>
    <p>Meine strukturierte Herangehensweise macht den Prozess für Sie transparenter. In jeder Phase des Verkaufs nehme ich mir die nötige Zeit, damit Sie danach sagen können:</p>
  </div>
  <div class="band" style="left:0;top:349px;width:177px;height:35px;font-size:8px;line-height:9.5px;text-align:left;justify-content:flex-start;padding-left:17px">Mit Hilfe von Marlene Brenner habe<br>ich den Käufer gefunden, der passt.</div>
  <div class="photo" style="left:0;top:392px;width:177px;height:113px" role="img" aria-label="Foto: Maklerin beim Schreiben am Tisch"></div>

  <!-- middle panel -->
  <div class="green-panel" style="left:177px;top:0;width:181px;height:384px"></div>
  <div class="slogan" style="left:177px;top:185px;width:181px;font-size:14.5px;line-height:17px">Ich nehme mir<br>Zeit für Sie!</div>
  <div class="contact-box" style="left:194px;top:246px;width:149px;height:103px">
    <div style="position:absolute;top:-6px;left:8px;right:8px;background:linear-gradient(90deg,#79a943,#8fbd48);text-align:center;font-size:7.6px;line-height:9.5px;padding:0 4px">Vereinbaren Sie einen unverbindlichen persönlichen Gesprächstermin mit mir:</div>
    <div class="contact-list">
      <div class="contact-row"><svg viewBox="0 0 24 24"><path fill="#fff" d="M6.6 10.8a15 15 0 006.6 6.6l2.2-2.2c.3-.3.7-.4 1-.2 1.1.4 2.3.6 3.6.6.6 0 1 .4 1 1V20c0 .6-.4 1-1 1A17 17 0 013 4c0-.6.4-1 1-1h3.5c.6 0 1 .4 1 1 0 1.3.2 2.5.6 3.6.1.3 0 .7-.2 1z"/></svg>01234 - 5678 900</div>
      <div class="contact-row"><svg viewBox="0 0 24 24"><path fill="#fff" d="M2 5h20v14H2zm2 2v.5l8 5 8-5V7l-8 5z"/></svg>info@brenner.immobilien</div>
      <div class="contact-row"><svg viewBox="0 0 24 24"><path fill="#fff" d="M12 2a7 7 0 00-7 7c0 5 7 13 7 13s7-8 7-13a7 7 0 00-7-7zm0 9.5A2.5 2.5 0 1112 6.5a2.5 2.5 0 010 5z"/></svg>Marktplatz 12 | 84000 Musterstadt</div>
    </div>
  </div>
  <div class="brand" style="left:177px;top:414px;width:181px;font-size:12px"><span class="dot"></span>Brenner Immobilien</div>
  <div class="url" style="left:177px;top:481px;width:181px">WWW.BRENNER.IMMOBILIEN</div>

  <!-- right panel -->
  <div class="brand" style="left:358px;top:70px;width:182px;font-size:12px"><span class="dot"></span>Brenner Immobilien</div>
  <div class="photo" style="left:361px;top:102px;width:179px;height:282px" role="img" aria-label="Porträtfoto der Maklerin"></div>
  <svg class="abs" style="left:358px;top:95px" width="182" height="290" viewBox="0 0 182 290">
    <path d="M0 6 Q90 14 182 10 L182 0 L0 0Z" fill="#fff"/>
    <path d="M0 6 Q90 14 182 10" stroke="var(--green-mid)" stroke-width="2" fill="none"/>
    <path d="M0 290 Q10 220 182 150 Q60 230 30 290Z" fill="var(--green-mid)"/>
  </svg>
  <div style="position:absolute;left:358px;top:384px;width:182px;height:121px;background:#fff"></div>
  <div style="position:absolute;left:358px;top:398px;width:182px;text-align:center;font-size:14px;color:var(--ink)">IMMOBILIENVERKAUF</div>
  <div style="position:absolute;left:428px;top:418px;width:42px;height:.8px;background:var(--green-mid)"></div>
  <div class="band" style="left:358px;top:431px;width:182px;height:42px;font-size:14.5px;line-height:17px;text-transform:uppercase">Ich nehme mir<br>Zeit für Sie!</div>
  <div class="url" style="left:358px;top:481px;width:182px">WWW.BRENNER.IMMOBILIEN</div>
  <svg class="abs" style="left:177px;top:492px" width="363" height="13" viewBox="0 0 363 13"><path d="M0 13 Q180 2 363 8 L363 13Z" fill="var(--green-mid)"/><path d="M0 13 Q180 6 363 12 L363 13Z" fill="#fff"/></svg>
</section>

<!-- ===== Inner side ===== -->
<section class="sheet sheet--inner">
  <!-- left column -->
  <svg class="icon" style="left:83px;top:12px" viewBox="0 0 24 24"><path fill="none" stroke="var(--green-mid)" stroke-width="1.6" d="M12 5a6 6 0 00-3.5 10.9V18h7v-2.1A6 6 0 0012 5zM9.5 21h5M12 8v5"/></svg>
  <div class="heading heading--green" style="left:0;top:36px;width:182px;font-size:8px">1) Sich klar werden</div>
  <div class="body-text" style="left:16px;top:62px;width:155px">
    <div class="subhead">Die eigene Verkaufsbereitschaft auf den Prüfstand stellen</div>
    <p>Neben der Klärung der Eigentumsverhältnisse, z.B. bei einer Erbengemeinschaft, geht es um Ihre Motivation und Verkaufsbereitschaft.</p>
    <p>Haben Sie alle Möglichkeiten wie Renovierung und Vermietung durchdacht und eine Rentabilitätsrechnung erstellt? Ist ein Verkauf die richtige Entscheidung?</p>
  </div>
  <div class="band" style="left:0;top:148px;width:182px;height:18px">Ich stelle Ihnen die passenden Fragen,<br>damit Sie sich klarwerden können.</div>

  <svg class="icon" style="left:83px;top:175px" viewBox="0 0 24 24"><path fill="none" stroke="var(--green-mid)" stroke-width="1.6" d="M5 3h11v18H5zM8 8h5M8 12h5M8 16h3M20 6l-6 9"/></svg>
  <div class="heading heading--green" style="left:0;top:199px;width:182px;font-size:8px">2) Maklerauftrag</div>
  <div class="body-text" style="left:16px;top:224px;width:155px">
    <div class="subhead">Ihre Ziele entscheiden über die Art des Auftrags</div>
    <p>Grundsätzlich können Sie sich entscheiden, ob Sie mich als Alleinmakler oder Nachweis- und Vermittlungsmakler beauftragen.</p>
    <p>Ihr Vorteil bei der Alleinvermarktung ist, dass ich im festgelegten Zeitraum nachweisbar für Ihren Immobilienverkauf tätig werden muss.</p>
  </div>
  <div class="band" style="left:0;top:308px;width:182px;height:18px">Die Transparenz durch die<br>Nachweisbarkeit gibt Ihnen Sicherheit.</div>

  <svg class="icon" style="left:83px;top:336px" viewBox="0 0 24 24"><path fill="var(--green-mid)" d="M12 2l2.9 6.6 7.1.6-5.4 4.7 1.6 7-6.2-3.7-6.2 3.7 1.6-7L2 9.2l7.1-.6z"/></svg>
  <div class="heading heading--green" style="left:0;top:360px;width:182px;font-size:8px">3) Immobilienbewertung</div>
  <div class="body-text" style="left:16px;top:386px;width:155px">
    <div class="subhead">Sich Zeit nehmen für Details</div>
    <p>Basis für eine erfolgreiche Präsentation ist die Bewertung Ihrer Immobilie. Für diese nehme ich mir viel Zeit.</p>
    <p>Neben einer Markteinschätzung fließen die baulichen Aspekte und die rechtlichen Gegebenheiten wie der Grundbuchauszug, die Bebauungsmöglichkeiten, die Vorgaben der Gemeinde/der Stadt und das Umfeld der Immobilie mit ein.</p>
  </div>
  <div class="band" style="left:0;top:471px;width:182px;height:18px">Gemeinsam arbeiten wir die Details für eine<br>erfolgreiche Verkaufs- &amp; Präsentationsstrategie aus.</div>

  <!-- middle column -->
  <div class="green-panel" style="left:182px;top:0;width:180px;height:505px;background:linear-gradient(90deg,var(--green-dark),var(--green-light))"></div>
  <svg class="icon" style="left:264px;top:12px" viewBox="0 0 24 24"><circle cx="12" cy="12" r="8" fill="none" stroke="#fff" stroke-width="1.6"/><path fill="none" stroke="#fff" stroke-width="1.6" d="M12 7v5l3 2"/></svg>
  <div class="heading" style="left:182px;top:36px;width:180px;font-size:8px;color:#fff">Zeit für Transparenz</div>
  <div class="mid-text" style="left:197px;top:62px;width:152px">
    <div style="font-weight:600;font-size:5.6px;margin-bottom:9px">WIE SCHAFFT MAN TRANSPARENZ?</div>
    <div style="margin-bottom:7px">Aus meiner Sicht, indem man zuhört und vermittelt. Und das in jeder Phase des Immobilienverkaufs.</div>
    <div style="width:20px;height:.6px;background:#fff;margin-bottom:7px"></div>
    <div>Für mich gibt es 6 wesentliche Schritte um das bestmögliche Verkaufsergebnis für Sie zu erreichen:</div>
  </div>
  <ul class="step-list abs" style="left:197px;top:141px;width:160px">
    <li><span>1</span>Sich klarwerden</li>
    <li><span>2</span>Richtige Art des Maklerauftrags festlegen</li>
    <li><span>3</span>Immobilienbewertung mit Detailbetrachtung</li>
    <li><span>4</span>Optimale Präsentation- und Verkaufsstrategie</li>
    <li><span>5</span>Besichtigung – den passenden Käufer finden</li>
    <li><span>6</span>Kaufvertrag aushandeln – Übergabe begleiten</li>
  </ul>
  <div class="mid-text" style="left:197px;top:250px;width:155px">Nehmen Sie sich die Zeit, diese Schritte gemeinsam mit mir „ZU DENKEN“.</div>
  <div class="slogan" style="left:182px;top:279px;width:180px;font-size:7.6px;line-height:10px">Der Prozess Ihres Verkaufs wird<br>so für Sie transparenter.</div>
  <div class="photo" style="left:222px;top:344px;width:100px;height:161px;background:linear-gradient(180deg,#d6b48a,#2e2e2e 60%)" role="img" aria-label="Porträtfoto der Maklerin in schwarzer Kleidung"></div>

  <!-- right column -->
  <svg class="icon" style="left:443px;top:12px" viewBox="0 0 24 24"><path fill="none" stroke="var(--green-mid)" stroke-width="1.6" d="M4 4h16v11H4zM12 15v5M8 20h8M7 12l3-3 3 2 4-5"/></svg>
  <div class="heading heading--green" style="left:362px;top:36px;width:178px;font-size:8px;text-align:center;line-height:10px">4) Präsentation- und<br>Verkaufsstrategie</div>
  <div class="body-text" style="left:374px;top:71px;width:156px">
    <div class="subhead">Den potentiellen Käufer optimal ansprechen</div>
    <p>Entsprechend der Zielgruppe für Ihre Immobilie arbeite ich die Präsentations- und Verkaufsstrategie auf Basis der Bewertung aus. Ein Eintrag in den bekannten Immobilienportalen reicht nicht immer. Ein ansprechendes Exposé, passende Außenwerbung, aber auch Diskretion wenn es notwendig ist, fließt in die Verkaufsstrategie mit ein.</p>
  </div>
  <div class="band" style="left:362px;top:138px;width:178px;height:28px">Die Bedürfnisse der potentiellen Käufer erkennen<br>und Ihre Immobilien entsprechend präsentieren,<br>ist der Schlüssel zum Verkaufserfolg.</div>

  <svg class="icon" style="left:443px;top:175px" viewBox="0 0 24 24"><circle cx="14" cy="10" r="6" fill="none" stroke="var(--green-mid)" stroke-width="1.8"/><circle cx="14" cy="10" r="2" fill="var(--green-mid)"/><path stroke="var(--green-mid)" stroke-width="2.4" d="M9.5 14.5L4 20"/></svg>
  <div class="heading heading--green" style="left:362px;top:199px;width:178px;font-size:8px">5) Besichtigungen</div>
  <div class="body-text" style="left:374px;top:224px;width:156px">
    <div class="subhead">Den passenden Käufer finden</div>
    <p>Fingerspitzengefühl ist bei den Besichtigungen gefragt, denn in den wenigsten Fällen ist die Immobilie freistehend. Nicht nur die Kaufbereitschaft, sondern auch der Kaufwille durch eine entsprechende Zusage der Bank ist wichtig bei der Vorauswahl der potentiellen Käufer.</p>
    <p>Das Ergebnis der Vorauswahl besprechen wir gemeinsam.</p>
  </div>
  <div class="band" style="left:362px;top:308px;width:178px;height:18px">Neben den Fakten ist mir wichtig, dass sie<br>nach dem Verkauf sagen können „das passt“.</div>

  <svg class="icon" style="left:443px;top:336px" viewBox="0 0 24 24"><path fill="var(--green-mid)" d="M2 8l5-3 5 3 5-3 5 3v5l-4 1-5 5-3-2-3-2-5-2z"/></svg>
  <div class="heading heading--green" style="left:362px;top:360px;width:178px;font-size:8px">6) Kaufvertrag aushandeln</div>
  <div class="body-text" style="left:374px;top:386px;width:156px">
    <div class="subhead">Übergabe begleiten</div>
    <p>Zuhören, Lösungen finden, sich Zeit nehmen – der Ausarbeitung des Kaufvertrags gehört die meiste Sorgfalt.</p>
    <p>Ich gebe Ihnen Antworten und zeige durch meine Erfahrung mit Notaren und auch Rechtsanwälten Möglichkeiten auf, um den Verkauf zu Ihrer vollsten Zufriedenheit abzuschließen.</p>
  </div>
  <div class="band" style="left:362px;top:471px;width:178px;height:18px">Nach der Schlüsselübergabe bin ich bei<br>Fragen weiterhin für Sie da.</div>
</section>

</body>
</html>
```